Cleaning Bochure for Different Services

We need to create preferably an A4 brochure for cleaning services so we are able to give to our customers upon meeting them. check out our website for more info. It is www.brightvalecare.co.uk We need a page on;-Commercial Cleaning-Carpet Cleaning-Oven Cleaning with description and some imagery.

Target Market(s)

Commercial Cleaning Customers

Industry/Entity Type

Office Cleaning

Font styles to use
Sans Serif

Colors
33a6d7
aaaaaa

Requirements
Must have
• 4 pages each containing these services
• -Commercial Cleaning (most important)
• -Carpet Cleaning
• -Oven Cleaning
Nice to have
• Clean and smart looking design use some imagination and possibly go wild!
• Must be eye catching!

```html
<!DOCTYPE html>
<html lang="en">
<head>
<meta charset="utf-8">
<title>Brightvale Care – Commercial Cleaning Brochure</title>
<link href="https://fonts.googleapis.com/css2?family=Open+Sans:wght@400;600;700&display=swap" rel="stylesheet">
<style>
:root{
  --brand:#33a6d7;
  --brand-deep:#1a6fb8;
  --brand-light:#8fd0ee;
  --grey:#aaaaaa;
  --grey-dark:#8c8c8c;
  --backdrop:#d6d7d9;
  --ink:#333333;
  --white:#ffffff;
}
*{box-sizing:border-box;margin:0;padding:0}
html,body{width:841px;height:1200px;overflow:hidden}
body{background:var(--backdrop);font-family:'Open Sans',sans-serif;color:var(--ink);position:relative}
.spread{position:absolute;left:49px;width:748px;height:528px;display:flex;box-shadow:0 6px 8px rgba(0,0,0,.18)}
.spread--outer{top:42px}
.spread--inner{top:618px}
.page{position:relative;width:374px;height:528px;background:var(--white);overflow:hidden}
.page + .page{box-shadow:inset 6px 0 8px -6px rgba(0,0,0,.15)}
.photo{position:absolute;left:0;width:100%}
.wave{position:absolute;left:0;width:100%}
.brand-name{position:absolute;font-weight:700;color:var(--brand);font-size:19px;letter-spacing:.2px;display:flex;align-items:center;gap:6px;white-space:nowrap}
.brand-name .dot{width:12px;height:12px;border-radius:50%;background:var(--grey)}
.heading{position:absolute;left:16px;color:var(--brand);font-size:17.5px;font-weight:400}
.subheading{position:absolute;left:18px;font-size:12px;color:var(--ink)}
.body-copy{position:absolute;font-size:7.6px;line-height:11.8px;text-align:justify;color:var(--ink)}
.body-copy p+p{margin-top:11px}
.ticks{position:absolute;list-style:none}
.ticks li{display:flex;align-items:center;gap:9px;font-size:9.4px;height:21.5px}
.ticks svg{width:22px;height:14px}
.cta{position:absolute;width:100%;text-align:center;font-size:9.4px;color:var(--brand)}
.cta--light{color:var(--white)}
.phone-pill{position:absolute;height:22px;border-radius:11px;background:linear-gradient(#c9c9c9,#9d9d9d);color:var(--white);font-weight:600;font-size:15.5px;display:flex;align-items:center;justify-content:center;gap:6px;box-shadow:0 1px 2px rgba(0,0,0,.3)}
.phone-pill svg{width:15px;height:15px}
.socials{position:absolute;left:0;width:100%;display:flex;justify-content:center;gap:10px}
.socials span{width:17px;height:17px;border-radius:50%;border:1.4px solid var(--white)}
.contact-line{position:absolute;width:100%;text-align:center;color:var(--white);font-size:9.6px;letter-spacing:.6px}
.badge{position:absolute;left:267px;top:337px;width:62px;height:30px;border-radius:3px;background:#2e3b7a}
.cover-title{position:absolute;width:100%;text-align:center;color:var(--white);font-weight:700;font-size:18.5px;letter-spacing:.4px;text-shadow:0 1px 2px rgba(0,0,0,.3)}
.cover-sub{position:absolute;width:100%;text-align:center;color:var(--white);font-size:14px}
.round-photo{position:absolute;border-radius:50%;border:4px solid var(--white);box-shadow:0 1px 3px rgba(0,0,0,.3)}
.round-photo--grey{border:5px solid var(--grey-dark)}
.round-label{position:absolute;width:100%;bottom:12px;text-align:center;color:var(--white);font-weight:700;font-size:9px}
</style>
</head>
<body>

<section class="spread spread--outer">
  <article class="page page--back">
    <div class="photo" style="top:0;height:172px;background:linear-gradient(180deg,#3e5870 0%,#5f6f7c 45%,#2a2e33 100%)" role="img" aria-label="Cleaning team in black uniforms standing in front of branded vans and the company unit"></div>
    <svg class="wave" style="top:150px;height:80px" viewBox="0 0 374 80" preserveAspectRatio="none"><path d="M0 18 Q187 -4 374 18 L374 80 L0 80Z" fill="#fff"/></svg>
    <div class="brand-name" style="left:116px;top:194px"><span class="dot"></span>Brightvale Care</div>
    <h2 class="heading" style="top:222px">The complete package</h2>
    <div class="body-copy" style="left:16px;top:258px;width:341px">
      <p>Brightvale Care Group Limited is a York based commercial cleaning company with a team of over 50 years experience. We create bespoke programs providing daily, weekly, fort-nightly or monthly services to domestic and commercial customers alike. Whether you are a business, tenant, landlord or homeowner our cleaning services are all in one place, saving you time and money.</p>
    </div>
    <ul class="ticks" style="left:16px;top:322px">
      <li><svg viewBox="0 0 22 14"><path d="M2 8 L8 12 L20 2" fill="none" stroke="var(--brand)" stroke-width="2.4" stroke-linecap="round"/></svg>Value for money</li>
      <li><svg viewBox="0 0 22 14"><path d="M2 8 L8 12 L20 2" fill="none" stroke="var(--brand)" stroke-width="2.4" stroke-linecap="round"/></svg>Bespoke packages to suit your needs</li>
      <li><svg viewBox="0 0 22 14"><path d="M2 8 L8 12 L20 2" fill="none" stroke="var(--brand)" stroke-width="2.4" stroke-linecap="round"/></svg>Local York Cleaning Business</li>
    </ul>
    <div class="badge"></div>
    <p class="cta" style="top:401px">Contact us today for a free no obligation quotation</p>
    <svg class="wave" style="top:408px;height:120px" viewBox="0 0 374 120" preserveAspectRatio="none">
      <defs><linearGradient id="backBlue" x1="0" y1="0" x2="0" y2="1"><stop offset="0" stop-color="#2f9bd6"/><stop offset="1" stop-color="#1765b2"/></linearGradient></defs>
      <path d="M0 30 Q187 0 374 14 L374 120 L0 120Z" fill="url(#backBlue)"/>
      <path d="M0 26 Q187 -4 374 10" fill="none" stroke="var(--brand-light)" stroke-width="2"/>
    </svg>
    <div class="socials" style="top:453px"><span></span><span></span><span></span></div>
    <div class="phone-pill" style="left:117px;top:478px;width:141px">
      <svg viewBox="0 0 16 16"><circle cx="8" cy="8" r="7" fill="none" stroke="#fff" stroke-width="1.4"/><path d="M5 4.5 L6.5 4.5 L7 6.5 L6 7.2 Q7 9.2 8.8 10 L9.5 9 L11.5 9.5 L11.5 11 Q7 11.5 5 6Z" fill="#fff"/></svg>01632 960 555
    </div>
    <p class="contact-line" style="top:505px">info@brightvalecare.co.uk | www.brightvalecare.co.uk</p>
  </article>

  <article class="page page--cover">
    <div class="brand-name" style="left:112px;top:40px;font-size:24px"><span class="dot" style="width:14px;height:14px"></span>Brightvale Care</div>
    <div class="photo" style="top:98px;height:340px;background:linear-gradient(180deg,#dfe5ea 0%,#b9c4cc 40%,#8b979f 100%)" role="img" aria-label="Bright modern open-plan office with desks, monitors and large windows"></div>
    <svg class="wave" style="top:80px;height:40px" viewBox="0 0 374 40" preserveAspectRatio="none"><path d="M0 0 L374 0 L374 22 Q187 40 0 18Z" fill="#fff"/></svg>
    <svg class="wave" style="top:380px;height:148px" viewBox="0 0 374 148" preserveAspectRatio="none">
      <defs><linearGradient id="coverBlue" x1="0" y1="0" x2="0" y2="1"><stop offset="0" stop-color="#2f9bd6"/><stop offset="1" stop-color="#1765b2"/></linearGradient></defs>
      <path d="M0 20 Q187 40 374 4 L374 148 L0 148Z" fill="var(--grey)"/>
      <path d="M0 26 Q187 46 374 12 L374 148 L0 148Z" fill="url(#coverBlue)"/>
    </svg>
    <div class="round-photo" style="left:56px;top:338px;width:88px;height:88px;background:radial-gradient(#c7a98a,#8a6d55)" role="img" aria-label="Mopping a tiled floor"></div>
    <div class="round-photo" style="left:140px;top:334px;width:92px;height:92px;background:radial-gradient(#efe9df,#c9beb0)" role="img" aria-label="Carpet being cleaned with an extraction wand"></div>
    <div class="round-photo" style="left:224px;top:338px;width:88px;height:88px;background:radial-gradient(#d89a5c,#4a6fb0)" role="img" aria-label="Cleaning a wooden floor with a blue bucket"></div>
    <h1 class="cover-title" style="top:440px">COMMERCIAL CLEANING SERVICES</h1>
    <p class="cover-sub" style="top:464px">The Complete Cleaning Solution</p>
    <div class="phone-pill" style="left:112px;top:493px;width:141px">
      <svg viewBox="0 0 16 16"><circle cx="8" cy="8" r="7" fill="none" stroke="#fff" stroke-width="1.4"/><path d="M5 4.5 L6.5 4.5 L7 6.5 L6 7.2 Q7 9.2 8.8 10 L9.5 9 L11.5 9.5 L11.5 11 Q7 11.5 5 6Z" fill="#fff"/></svg>01632 960 555
    </div>
  </article>
</section>

<section class="spread spread--inner">
  <article class="page page--commercial">
    <div class="photo" style="top:0;height:200px;background:linear-gradient(180deg,#eef2f5 0%,#a8b6c2 50%,#3f5466 100%)" role="img" aria-label="Silhouette of a cleaner with a trolley in a glass-walled terminal"></div>
    <svg class="wave" style="top:130px;height:100px" viewBox="0 0 374 100" preserveAspectRatio="none">
      <path d="M0 30 Q120 80 374 20 L374 100 L0 100Z" fill="var(--brand-light)"/>
      <path d="M0 38 Q130 84 374 40 L374 100 L0 100Z" fill="var(--brand)"/>
      <path d="M0 46 Q140 96 374 50 L374 100 L0 100Z" fill="#fff"/>
    </svg>
    <h2 class="heading" style="top:228px">Commercial Cleaning in York</h2>
    <div class="body-copy" style="left:17px;top:264px;width:340px">
      <p>We create bespoke packages to suit each individual businesses needs. Whether you require cleaning daily, weekly, fortnightly or monthly we are happy to create a bespoke package for you.</p>
      <p style="margin-top:24px">Brightvale Care constantly strives to be the most efficient and effective commercial clean-ing service in York. We are accustomed to managing a diverse array of accounts from large organisations to family businesses.</p>
      <p style="margin-top:24px">We understand that the size of the business alone doesn’t define the nature and complex-ity of the cleaning tasks required. Therefore, we hold thorough discussions with opera-tions management and carry out a cleaning requirements audit of the premises before initiating the contract.</p>
    </div>
    <ul class="ticks" style="left:17px;top:422px">
      <li><svg viewBox="0 0 22 14"><path d="M2 8 L8 12 L20 2" fill="none" stroke="var(--brand)" stroke-width="2.4" stroke-linecap="round"/></svg>Hassle free contract transfer (TUPE)</li>
      <li><svg viewBox="0 0 22 14"><path d="M2 8 L8 12 L20 2" fill="none" stroke="var(--brand)" stroke-width="2.4" stroke-linecap="round"/></svg>Value for money</li>
      <li><svg viewBox="0 0 22 14"><path d="M2 8 L8 12 L20 2" fill="none" stroke="var(--brand)" stroke-width="2.4" stroke-linecap="round"/></svg>Bespoke packages</li>
    </ul>
    <div class="brand-name" style="right:18px;top:450px;font-size:16px"><span class="dot"></span>Brightvale Care</div>
    <svg class="wave" style="top:484px;height:44px" viewBox="0 0 374 44" preserveAspectRatio="none">
      <path d="M0 16 Q187 -2 374 12 L374 44 L0 44Z" fill="var(--grey)"/>
      <path d="M0 20 Q187 4 374 16 L374 44 L0 44Z" fill="var(--brand-deep)"/>
    </svg>
  </article>

  <article class="page page--carpet-oven">
    <div class="photo" style="top:0;height:170px;background:linear-gradient(180deg,#6d7588 0%,#8c93a3 60%,#7a8293 100%)" role="img" aria-label="Grey office carpet being cleaned with an extraction wand"></div>
    <svg class="wave" style="top:120px;height:70px" viewBox="0 0 374 70" preserveAspectRatio="none">
      <path d="M0 40 Q200 0 374 40 L374 70 L0 70Z" fill="var(--grey)"/>
      <path d="M0 46 Q200 6 374 52 L374 70 L0 70Z" fill="#fff"/>
    </svg>
    <h2 class="heading" style="left:18px;top:158px">Commercial Carpet Cleaning</h2>
    <p class="subheading" style="top:180px">Putting a spring back in your step.</p>
    <div class="body-copy" style="left:18px;top:209px;width:340px">
      <p>Whether it being a bar, pub, restaurant, cinema, casino, bingo hall, office or educational facility we have the expertise to ensure your carpets are correctly cleaned.</p>
      <p style="margin-top:6px">Our professional and affordable York Carpet Cleaning Service will use a selection of tailored techniques to ensure carpets are returned to pristine condition with no shrinkage and fast drying time.</p>
    </div>
    <ul class="ticks" style="left:18px;top:283px">
      <li><svg viewBox="0 0 22 14"><path d="M2 8 L8 12 L20 2" fill="none" stroke="var(--brand)" stroke-width="2.4" stroke-linecap="round"/></svg>Zero Shrinkage</li>
      <li><svg viewBox="0 0 22 14"><path d="M2 8 L8 12 L20 2" fill="none" stroke="var(--brand)" stroke-width="2.4" stroke-linecap="round"/></svg>Fast drying time</li>
      <li><svg viewBox="0 0 22 14"><path d="M2 8 L8 12 L20 2" fill="none" stroke="var(--brand)" stroke-width="2.4" stroke-linecap="round"/></svg>Increases life of carpets</li>
    </ul>
    <div class="round-photo round-photo--grey" style="left:259px;top:272px;width:96px;height:96px;background:radial-gradient(#5a4a3a,#1f1a16)" role="img" aria-label="Dirty oven interior before cleaning"><span class="round-label">BEFORE</span></div>
    <div class="round-photo round-photo--grey" style="left:259px;top:360px;width:96px;height:96px;background:radial-gradient(#9aa0a6,#2b2e31)" role="img" aria-label="Clean oven interior after cleaning"><span class="round-label">AFTER</span></div>
    <h2 class="heading" style="left:18px;top:367px">Oven Cleaning</h2>
    <p class="subheading" style="top:389px">In partnership with Oven Revive.</p>
    <div class="body-copy" style="left:18px;top:410px;width:240px;text-align:left">
      <p>Tenants landlords and agents alike.</p>
      <p style="margin-top:6px">Yorkshires leading oven cleaning and repair specialists. Have your oven cleaned from as little as £45.00 (inc vat)!</p>
    </div>
    <svg class="wave" style="top:456px;height:72px" viewBox="0 0 374 72" preserveAspectRatio="none">
      <defs><linearGradient id="innerBlue" x1="0" y1="0" x2="0" y2="1"><stop offset="0" stop-color="#2f9bd6"/><stop offset="1" stop-color="#1765b2"/></linearGradient></defs>
      <path d="M0 26 Q187 0 374 22 L374 72 L0 72Z" fill="var(--grey)"/>
      <path d="M0 32 Q187 8 374 30 L374 72 L0 72Z" fill="url(#innerBlue)"/>
    </svg>
    <p class="cta cta--light" style="top:484px">Contact us today for a free no obligation quotation</p>
    <div class="phone-pill" style="left:112px;top:503px;width:141px">
      <svg viewBox="0 0 16 16"><circle cx="8" cy="8" r="7" fill="none" stroke="#fff" stroke-width="1.4"/><path d="M5 4.5 L6.5 4.5 L7 6.5 L6 7.2 Q7 9.2 8.8 10 L9.5 9 L11.5 9.5 L11.5 11 Q7 11.5 5 6Z" fill="#fff"/></svg>01632 960 555
    </div>
  </article>
</section>

</body>
</html>
```